looking for sleek business card to standout from the crowd!

We are a young biotechnology company looking to help you personalize your health through understanding your genetic make up. We need you help in making a clean but sleek business card design using our new logo. The goal? Any time we give our cards out, people say "nice card!" The feel we are going for is "modern-techy". We don't want to come across as an old, giant pharma company, but not trying to be a hipster either.

Target Market(s)

healthcare and biotechnology industry.

Industry/Entity Type

Biotechnology

Contact Information for Business Card

Info to include on the card will be NAME, TITLE, EMAIL, PHONE. The companies website (www.corvalinbio.com) should also be on the card some where. Would like the logo, when printed, to be raised.

Requirements
Must have
• The logo we have attached in the color it is in. Fonts for text should lean toward more professional/tech.
Nice to have
• Prefer white/light color background
Should not have
• cartoons, landscape backgrounds images.

```html
<!DOCTYPE html>
<html lang="en">
<head>
<meta charset="utf-8">
<title>Corvalin Business Card</title>
<link rel="stylesheet" href="https://fonts.googleapis.com/css2?family=Open+Sans:wght@400;600;700&display=swap">
<style>
  :root {
    --backdrop: #cacacd;
    --lime: #8cc540;
    --blue: #0b73bb;
    --ink: #3a3a3a;
    --rule: #555555;
    --white: #ffffff;
  }
  * { margin: 0; padding: 0; box-sizing: border-box; }
  html, body {
    width: 1200px; height: 1200px; overflow: hidden;
    background: var(--backdrop);
    font-family: "Open Sans", Arial, sans-serif;
  }
  .sheet {
    position: relative; width: 1200px; height: 1200px;
  }
  .card {
    position: absolute; left: 160px; width: 880px; height: 500px;
    box-shadow: 0 6px 18px rgba(0,0,0,0.22);
    overflow: hidden;
  }
  .card--front { top: 60px; background: var(--lime); }
  .card--back { top: 630px; background: var(--white); }

  .wordmark {
    display: flex; align-items: center; gap: 14px;
    font-weight: 700; color: var(--blue); letter-spacing: 1px;
  }
  .wordmark__dot {
    border-radius: 50%; background: var(--white); flex: none;
  }
  .card--front .wordmark {
    position: absolute; left: 50%; top: 50%; transform: translate(-50%, -50%);
    font-size: 62px;
  }
  .card--front .wordmark__dot { width: 56px; height: 56px; }

  .card--back .wordmark {
    position: absolute; left: 90px; top: 222px; font-size: 44px;
  }
  .card--back .wordmark__dot { width: 42px; height: 42px; background: var(--lime); }

  .divider {
    position: absolute; left: 440px; top: 110px; width: 2px; height: 230px;
    background: var(--rule);
  }
  .details {
    position: absolute; left: 470px; top: 104px; color: var(--ink);
  }
  .details__name { font-size: 30px; font-weight: 600; color: var(--lime); line-height: 1.1; }
  .details__title { font-size: 16px; margin-top: 2px; }
  .details__address { font-size: 18px; line-height: 1.3; margin-top: 22px; }
  .details__contacts { list-style: none; margin-top: 20px; font-size: 18px; line-height: 1.4; }
  .details__contacts li { display: flex; align-items: center; gap: 10px; }
  .details__contacts svg { width: 16px; height: 16px; flex: none; }

  .band { position: absolute; bottom: 0; }
  .band--blue { left: 0; width: 560px; height: 30px; background: var(--blue); }
  .band--lime { right: 0; width: 320px; height: 46px; background: var(--lime); }
  .band__dot {
    position: absolute; left: 542px; bottom: 20px; width: 36px; height: 36px;
    border-radius: 50%; background: var(--lime); border: 3px solid var(--white);
  }
</style>
</head>
<body>
<main class="sheet">
  <section class="card card--front" aria-label="Card front">
    <div class="wordmark"><span>CORVALIN</span><span class="wordmark__dot"></span></div>
  </section>

  <section class="card card--back" aria-label="Card back">
    <div class="wordmark"><span>CORVALIN</span><span class="wordmark__dot"></span></div>
    <div class="divider"></div>
    <div class="details">
      <p class="details__name">Dana Whitfield</p>
      <p class="details__title">President</p>
      <p class="details__address">55 demo street, demo place<br>P.O. Box 000, 555 Avenue</p>
      <ul class="details__contacts">
        <li>
          <svg viewBox="0 0 16 16" aria-hidden="true"><path fill="#8cc540" d="M3.5 1.5l2.5 3-1.5 1.5c.8 2 2.5 3.7 4.5 4.5L10.5 9l3 2.5-1.5 2.5C7 13.5 2.5 9 2 3z"/></svg>
          (555) 014-2290
        </li>
        <li>
          <svg viewBox="0 0 16 16" aria-hidden="true"><rect x="1" y="3.5" width="14" height="9" fill="#8cc540"/><path d="M1 3.5l7 5 7-5" fill="none" stroke="#fff" stroke-width="1.3"/></svg>
          info@yourwebsite.com
        </li>
        <li>
          <svg viewBox="0 0 16 16" aria-hidden="true"><circle cx="8" cy="8" r="7" fill="#8cc540"/><path d="M1 8h14M8 1c-3 3.5-3 10.5 0 14M8 1c3 3.5 3 10.5 0 14" fill="none" stroke="#fff" stroke-width="1"/></svg>
          www.yourwebsite.com
        </li>
      </ul>
    </div>
    <div class="band band--blue"></div>
    <div class="band band--lime"></div>
    <div class="band__dot"></div>
  </section>
</main>
</body>
</html>
```